DuePoint.com website design

We are a collection agency that collects debt from past residents of apartments on behalf of Property Management Companies. We are want to design a 3 page website with - Home - How it Works - Schedule Demo. We'd like a sketch of a skyline showing high rise apartment buildings, houses, shops, etc. We would like for there to be some animation, possibly clouds and the sun slowly moving. Maybe kids playing ball or catch or something like that. Bird flying and landing. An electric car charging (to indicate we are modern). We are looking for a friendly community vibe. The site will also need a button "Property Managers Login". When some comes to the site we would like a pop up that says "Property Managers Click Here/Past Residents Click Here" with a different icon for each that relates to the description. I've included a link to a test site we had designed so feel free to use some of the copy from it. We just aren't happy with the design. On the Home page our tag line should be "Get more payments, faster, from past residents!" and "Digital First, NOT Digital Only". All without transaction fees, we don't get paid unless we get you paid first!
Additional selling points:

24 hour virtual agent and virtual telephone agent so we don't miss any opportunities to GET YOUR MONEY!

Old school collection strategies meet cutting edge technology to create effective work flow algorithms to put the best debt collectors on your accounts with data driven intelligence to determine the best way to get paid.

No Subscription Fees
No Payment Processing Fees
No Software Fees
No Mail, Email or TXT Fees

Inquire about our FIRST PARTY accounts receivable outsourcing. You may qualify for free post move out A/R processing and AI payment negotiator for the low hanging fruit. Don't pay full collection commission when there wasn't a full collection attempt!

For the How it Works page - See the page from our previous design. I will include the link below. Please come up with your own version of this but you can use the copy from this page.

The schedule demo page will be a form that will feed to our CRM that will include:
Name
Email
Company
Title
Phone Number
Number of Units
Tell us how we can help you: (a box for them provide details)

Also include our phone number at the bottom with something like

Here is a link to our previous design test site:
https://brelmora-preview.example/duepoint-new/
I've attached an image of the back end so you can get an idea of the colors we need, I've also included our logo. For the most part we would like most of the site to match the blue colors from our logo, but we do need to incorporate some of the yellow in the images I've attached. Possibly make the buttons on the site the yellow color? Make the sun Match the yellow? I'll leave it up to you.

```html
<!DOCTYPE html>
<html lang="en">
<head>
<meta charset="utf-8">
<title>DuePoint.com</title>
<link href="https://fonts.googleapis.com/css2?family=Montserrat:wght@400;500;600;700;800;900&display=swap" rel="stylesheet">
<style>
:root{
  --navy:#15305c;
  --navy-deep:#0f2547;
  --teal:#5fb3cc;
  --teal-dark:#3f93ad;
  --sky:#e4f2f8;
  --sky-mid:#cfe7f1;
  --ink:#1b1f2a;
  --text:#3b4657;
  --white:#ffffff;
  --yellow:#f5c518;
}
*{box-sizing:border-box;margin:0;padding:0}
html,body{width:1200px;height:2908px;overflow:hidden}
body{font-family:"Montserrat",sans-serif;color:var(--text);background:var(--white);position:relative}
.abs{position:absolute}

/* header */
.site-header{left:0;top:0;width:1200px;height:80px;background:var(--white);display:flex;align-items:center;padding:0 40px;box-shadow:0 2px 6px rgba(0,0,0,.05);z-index:3}
.brand{display:flex;align-items:center;gap:10px;font-weight:800;font-size:24px;color:var(--navy)}
.brand-dot{width:30px;height:30px;border-radius:50%;background:var(--teal)}
.main-nav{display:flex;gap:36px;margin-left:200px;font-size:14px;font-weight:600;color:var(--navy)}
.main-nav .active{border-bottom:2px solid var(--navy);padding-bottom:4px}
.header-actions{margin-left:auto;display:flex;align-items:center;gap:24px;font-size:14px;font-weight:600;color:var(--navy)}
.login{display:flex;align-items:center;gap:6px}
.btn{display:inline-block;font-weight:700;font-size:13px;letter-spacing:.5px;text-transform:uppercase;padding:12px 22px;border-radius:3px}
.btn-teal{background:var(--teal);color:var(--white);text-transform:none;font-size:14px}

/* hero */
.hero{left:0;top:80px;width:1200px;height:640px;background:linear-gradient(#ffffff 0%,#f4fafd 100%)}
.hero-skyline{left:0;top:250px;width:1200px;height:390px;background:linear-gradient(180deg,rgba(207,231,241,.2),rgba(95,179,204,.35))}
.hero-title{left:0;top:160px;width:1200px;text-align:center;font-weight:900;font-size:62px;line-height:1.08;color:var(--ink);text-transform:uppercase}
.hero-sub{left:0;top:305px;width:1200px;text-align:center;font-weight:500;font-size:40px;color:var(--teal-dark);text-transform:uppercase}
.hero-band{left:160px;top:480px;width:880px;height:82px;background:var(--teal);display:flex;align-items:center;padding:0 40px;gap:20px}
.hero-band p{color:var(--white);font-weight:700;font-size:14px;line-height:1.5;text-transform:uppercase;width:360px}
.hero-band .btn{margin-left:auto;background:var(--navy);color:var(--white)}
.hero-band .btn + .btn{margin-left:0;background:transparent;border:2px solid var(--white)}

/* about */
.about{left:0;top:720px;width:1200px;height:420px;background:var(--sky)}
.section-label{display:flex;align-items:center;gap:14px;font-weight:800;font-size:30px;color:var(--ink);text-transform:uppercase}
.section-label::before{content:"";width:40px;height:3px;background:var(--ink)}
.about .section-label{left:160px;top:60px}
.about-copy{left:160px;top:112px;width:430px;font-size:13px;line-height:1.6}
.about-copy p+p{margin-top:16px}
.about .btn{left:160px;top:335px;background:var(--navy);color:var(--white)}
.about-accent{left:900px;top:30px;width:150px;height:150px;background:var(--navy)}
.about-photo{left:720px;top:50px;width:310px;height:310px;background:linear-gradient(160deg,#9cc6dc,#4d7592 60%,#2b3f56)}

/* selling points */
.points-title{left:0;top:1228px;width:1200px;display:flex;justify-content:center;align-items:center;gap:16px;font-weight:800;font-size:30px;color:var(--ink);text-transform:uppercase}
.points-title::before,.points-title::after{content:"";width:40px;height:3px;background:var(--ink)}
.agent-card{left:360px;top:1310px;width:480px;height:220px;background:var(--white);border:1px solid #d8dde3;box-shadow:0 6px 18px rgba(0,0,0,.08);text-align:center;padding-top:24px}
.agent-card p{font-size:21px;line-height:1.4;color:var(--ink);padding:0 30px;margin-top:14px}
.strategy-band{left:0;top:1560px;width:1200px;height:200px;background:linear-gradient(90deg,var(--sky),var(--sky-mid),var(--sky))}
.strategy-band p{position:absolute;left:240px;top:20px;width:720px;height:160px;background:var(--teal);color:var(--white);font-weight:700;font-size:15.5px;line-height:1.8;text-align:center;text-transform:uppercase;padding:22px 34px}
.fees-bg{left:0;top:1760px;width:1200px;height:520px;background:linear-gradient(#f7fbfd,#eaf4f8)}
.fee-card{width:200px;height:220px;background:var(--white);border:1px solid #d8dde3;box-shadow:0 4px 12px rgba(0,0,0,.08);text-align:center;padding-top:28px;font-size:17px;font-weight:500;line-height:1.3;color:var(--ink)}
.fee-card svg{display:block;margin:0 auto 26px}
.inquire-band{left:240px;top:2300px;width:720px;height:150px;background:var(--teal);color:var(--white);font-weight:700;font-size:14.5px;line-height:1.8;text-align:center;text-transform:uppercase;padding:20px 30px}
.community-scene{left:0;top:2450px;width:1200px;height:280px;background:linear-gradient(180deg,#f2f8fb 0%,#cfe7f1 55%,#8cc0d4 100%)}

/* footer */
.site-footer{left:0;top:2730px;width:1200px;height:178px;background:var(--navy-deep);color:#c9d4e3}
.site-footer .brand{position:absolute;left:160px;top:24px;color:var(--white);font-size:22px}
.footer-about{left:160px;top:70px;width:220px;font-size:12px;line-height:1.6}
.footer-col{top:22px;width:180px;font-size:12px;line-height:1.7}
.footer-col h4{font-size:17px;font-weight:700;color:var(--white);text-transform:uppercase;margin-bottom:6px;display:flex;align-items:center;gap:8px}
.footer-col h4::before{content:"";width:18px;height:2px;background:var(--white)}
.copyright{left:0;top:156px;width:1200px;text-align:center;font-size:10px;color:#8796ad;border-top:1px solid #23406c;padding-top:5px}
</style>
</head>
<body>

<header class="site-header abs">
  <div class="brand"><span class="brand-dot"></span>DuePoint</div>
  <nav class="main-nav">
    <span class="active">Home</span><span>How it Works</span><span>About Us</span><span>Contact</span>
  </nav>
  <div class="header-actions">
    <span class="login">
      <svg width="16" height="16" viewBox="0 0 16 16" fill="none" stroke="currentColor" stroke-width="1.6"><circle cx="8" cy="5" r="3"/><path d="M2 15c0-3.3 2.7-5 6-5s6 1.7 6 5"/></svg>
      Log In
    </span>
    <span class="btn btn-teal">Past Residents Click Here</span>
  </div>
</header>

<section class="hero abs">
  <div class="hero-skyline abs" role="img" aria-label="Line sketch of a city skyline with high-rise apartments, houses, shops, clouds and sun"></div>
  <h1 class="hero-title abs">Get more payments,<br>faster, from past residents!</h1>
  <p class="hero-sub abs">And “Digital First, NOT Digital Only”.</p>
  <div class="hero-band abs">
    <p>All without transaction fees, we don't get paid unless we get you paid first!</p>
    <span class="btn">Learn More</span>
    <span class="btn">Get Started Now</span>
  </div>
</section>

<section class="about abs">
  <h2 class="section-label abs">About Us</h2>
  <div class="about-copy abs">
    <p>Lorem Ipsum is simply dummy text of the printing and typesetting industry. Lorem Ipsum has been the industry's standard dummy text ever since the 1500s, when an unknown printer took a galley of type and scrambled it to make a type specimen book. It has survived not only five centuries. Lorem Ipsum has been the industry's standard dummy text ever since the 1500s.</p>
    <p>Lorem Ipsum is simply dummy text of the printing and typesetting industry. Lorem Ipsum.</p>
  </div>
  <span class="btn abs">Read More</span>
  <div class="about-accent abs"></div>
  <div class="about-photo abs" role="img" aria-label="Photo of high-rise apartment towers in a city"></div>
</section>

<h2 class="points-title abs">Additional Selling Points:</h2>
<div class="agent-card abs">
  <svg width="54" height="54" viewBox="0 0 54 54" fill="none" stroke="#3f93ad" stroke-width="3">
    <path d="M10 32V26a17 17 0 0 1 34 0v6"/>
    <rect x="6" y="28" width="9" height="14" rx="3"/>
    <rect x="39" y="28" width="9" height="14" rx="3"/>
    <path d="M44 42c0 5-6 7-13 7"/>
    <text x="27" y="32" font-family="Montserrat,sans-serif" font-size="11" font-weight="700" fill="#3f93ad" stroke="none" text-anchor="middle">24</text>
  </svg>
  <p>24 hour virtual agent and virtual telephone agent so we don't miss any opportunities to GET YOUR MONEY!</p>
</div>

<div class="strategy-band abs">
  <p>Old school collection strategies meet cutting edge technology to create effective work flow algorithms to put the best debt collectors on your accounts with data driven intelligence to determine the best way to get paid.</p>
</div>

<div class="fees-bg abs"></div>
<div class="fee-card abs" style="left:320px;top:1800px">
  <svg width="70" height="70" viewBox="0 0 70 70" fill="none" stroke="#15305c" stroke-width="3"><circle cx="35" cy="35" r="30"/><rect x="22" y="24" width="26" height="22" rx="2"/><path d="M13 57L57 13"/></svg>
  No Subscription<br>Fees
</div>
<div class="fee-card abs" style="left:680px;top:1800px">
  <svg width="70" height="70" viewBox="0 0 70 70" fill="none" stroke="#15305c" stroke-width="3"><circle cx="35" cy="35" r="30"/><rect x="19" y="25" width="32" height="20" rx="2"/><path d="M19 31h32M13 57L57 13"/></svg>
  No Payment<br>Processing Fees
</div>
<div class="fee-card abs" style="left:320px;top:2050px">
  <svg width="70" height="70" viewBox="0 0 70 70" fill="none" stroke="#15305c" stroke-width="3"><circle cx="35" cy="35" r="30"/><rect x="20" y="22" width="30" height="20" rx="2"/><path d="M28 48h14M13 57L57 13"/></svg>
  No Software<br>Fees
</div>
<div class="fee-card abs" style="left:680px;top:2050px">
  <svg width="70" height="70" viewBox="0 0 70 70" fill="none" stroke="#15305c" stroke-width="3"><circle cx="35" cy="35" r="30"/><rect x="19" y="24" width="32" height="22" rx="2"/><path d="M19 26l16 11 16-11M13 57L57 13"/></svg>
  No Mail, Email or<br>TXT Fees
</div>

<p class="inquire-band abs">Inquire about our first party accounts receivable outsourcing. You may qualify for free post move out A/R processing and AI payment negotiator for the low hanging fruit. Don't pay full collection commission when there wasn't a full collection attempt!</p>

<div class="community-scene abs" role="img" aria-label="Illustration of a neighbourhood with trees, wind turbines and a blue electric car at a charging station"></div>

<footer class="site-footer abs">
  <div class="brand"><span class="brand-dot"></span>DuePoint</div>
  <p class="footer-about abs">Lorem Ipsum is simply dummy text of the printing and typesetting industry. Lorem ipsum.</p>
  <div class="footer-col abs" style="left:470px">
    <h4>Useful Links</h4>
    <div>Home</div><div>How it Works</div><div>About Us</div><div>Contact</div>
  </div>
  <div class="footer-col abs" style="left:690px">
    <h4>Services</h4>
    <div>Lorem Ipsum</div><div>Lorem Ipsum</div><div>Lorem Ipsum</div><div>Lorem Ipsum</div>
  </div>
  <div class="footer-col abs" style="left:900px">
    <h4>Contact Us</h4>
    <div>Lorem Ipsum is simply dummy text of the printing</div>
    <div>(555) 014-2290</div>
    <div>hello@duepoint.example</div>
  </div>
  <p class="copyright abs">Copyright 2024 · DuePoint.com, LLC · All rights reserved</p>
</footer>

</body>
</html>
```